Tessavale Communications

I need a very clean, uncomplicated design for an LA-based, very senior level strategic communications firm with about four associates. Landing page should stress LA, maybe a slider with downtown skyline, Malibu pier, and Rodeo Drive. In addition to landing page with firm's description, all else we'd need is services offered page and another for bios of associates.

Industry/Entity Type

Communications

Font styles to use
Sans Serif

```html
<!DOCTYPE html>
<html lang="en">
<head>
<meta charset="utf-8">
<title>Tessavale Communications</title>
<link rel="stylesheet" href="https://fonts.googleapis.com/css2?family=Open+Sans:wght@400;600;700&display=swap">
<style>
:root{
  --brand:#1f6aa5;
  --ink:#222;
  --text:#666;
  --muted:#888;
  --nav:#555;
  --panel:#f4f4f4;
  --band:#ececec;
  --rule:#d6d6d6;
  --dark:#2b2a2a;
  --footer-text:#c9c9c9;
  --white:#fff;
}
*{box-sizing:border-box;margin:0;padding:0}
html,body{width:1150px;height:1200px;overflow:hidden}
body{position:relative;background:var(--white);font-family:"Open Sans",sans-serif;color:var(--text)}
a{text-decoration:none;color:inherit}

.site-header{position:absolute;left:0;top:0;width:1150px;height:133px;background:var(--white);border-bottom:2px solid #e4e4e4}
.brand{position:absolute;left:96px;top:23px;display:flex;align-items:center;gap:12px}
.brand-mark{width:64px;height:64px;border-radius:50%;background:var(--brand)}
.brand-name{color:var(--brand);font-weight:600;font-size:24px;line-height:28px;letter-spacing:-.3px}
.main-nav{position:absolute;right:96px;top:46px;display:flex;gap:36px}
.main-nav a{font-size:14px;color:var(--nav);text-transform:uppercase}
.main-nav a.active{color:var(--brand)}

.hero-band{position:absolute;left:0;top:135px;width:1150px;height:410px;background:var(--band);border-bottom:2px solid #e0e0e0}
.slider{position:absolute;left:95px;top:117px;width:960px;height:445px;overflow:hidden}
.slide-photo{position:absolute;inset:0;background:linear-gradient(180deg,#5f5a8f 0%,#6a5a8a 30%,#8a6a7a 52%,#b07860 68%,#7b5a6a 85%,#4c3d55 100%)}
.slide-caption{position:absolute;left:0;bottom:0;width:100%;height:55px;background:rgba(20,20,25,.78);color:var(--white);font-size:19px;font-weight:600;text-align:center;line-height:55px;letter-spacing:.2px}
.slide-arrow{position:absolute;bottom:0;width:45px;height:55px;display:flex;align-items:center;justify-content:center}
.slide-arrow.prev{left:0;background:rgba(0,0,0,.55)}
.slide-arrow.next{right:0}

.welcome-photo{position:absolute;left:95px;top:598px;width:224px;height:222px;background:linear-gradient(160deg,#e8eef3 0%,#c9d3db 45%,#5d6670 75%,#2f3238 100%)}
.welcome{position:absolute;left:333px;top:590px;width:478px}
.welcome h1{color:var(--brand);font-weight:600;font-size:26px;line-height:36px;white-space:nowrap}
.welcome h2{color:var(--ink);font-weight:600;font-size:15px;line-height:20px;margin-bottom:10px}
.welcome p{font-size:13px;line-height:22px;margin-bottom:8px}

.news{position:absolute;left:823px;top:590px;width:232px}
.news h3{font-weight:400;font-size:19px;color:var(--ink);line-height:28px;margin-bottom:5px}
.news-list{list-style:none;background:var(--panel);border-top:4px solid #666;height:205px;padding:16px 0 0 0}
.news-list li{position:relative;padding-left:34px;margin-bottom:14px}
.news-list li::before{content:"›";position:absolute;left:14px;top:-3px;font-size:17px;color:var(--ink)}
.news-title{display:block;font-size:15px;color:var(--ink);line-height:22px}
.news-date{display:block;font-size:13px;color:var(--muted);line-height:18px}

.site-footer{position:absolute;left:0;top:855px;width:1150px;height:240px;background:var(--panel)}
.foot-col{position:absolute;top:25px;height:198px}
.foot-col h4{font-weight:400;font-size:17px;color:#333;margin-bottom:16px;line-height:24px}
.foot-col p{font-size:12px;line-height:20px;color:var(--muted)}
.foot-col .lead{font-weight:600;color:#444;font-size:13px}
.foot-col .more{display:block;color:var(--brand);font-size:12px;margin-top:6px}
.divider{position:absolute;top:25px;width:1px;height:198px;background:var(--rule)}
.signup-field{width:198px;height:28px;background:var(--white);border:1px solid #cfcfcf;font-size:11px;color:#333;padding-left:15px;line-height:26px;margin-bottom:13px}
.signup-btn{position:absolute;left:130px;top:148px;width:68px;height:28px;background:linear-gradient(#8a8a8a,#666);color:var(--white);font-weight:600;font-size:13px;text-align:center;line-height:28px;box-shadow:0 1px 2px rgba(0,0,0,.3)}
.social{list-style:none}
.social li{display:flex;align-items:center;height:26px;margin-bottom:14px;font-size:12px;color:var(--muted)}
.social .badge{width:26px;height:26px;margin-right:10px;border-radius:2px}
.social .net{font-size:14px;margin-left:4px}
.net.blue{color:#2e5597}.net.sky{color:#2aa7e0}.net.navy{color:#1b6aa9}.net.red{color:#b4221a}

.base-bar{position:absolute;left:0;top:1095px;width:1150px;height:105px;background:var(--dark);text-align:center;color:var(--footer-text);font-size:12px}
.base-nav{margin-top:26px;word-spacing:2px}
.base-nav span{margin:0 9px}
.copyright{margin-top:17px;word-spacing:2px}
</style>
</head>
<body>
<header class="site-header">
  <div class="brand">
    <div class="brand-mark"></div>
    <div class="brand-name">Tessavale<br>Communications</div>
  </div>
  <nav class="main-nav">
    <a class="active" href="#">Home</a><a href="#">About Us</a><a href="#">Services</a><a href="#">Associates</a><a href="#">Contact Us</a>
  </nav>
</header>

<div class="hero-band"></div>
<section class="slider">
  <div class="slide-photo" role="img" aria-label="Downtown Los Angeles skyline lit at dusk with mountains behind"></div>
  <div class="slide-caption">WE ARE A SENIOR LEVEL STRATEGIC COMMUNICATIONS FIRM.</div>
  <a class="slide-arrow prev" href="#"><svg width="20" height="38" viewBox="0 0 20 38"><polyline points="18,1 2,19 18,37" fill="none" stroke="#fff" stroke-width="2"/></svg></a>
  <a class="slide-arrow next" href="#"><svg width="20" height="38" viewBox="0 0 20 38"><polyline points="2,1 18,19 2,37" fill="none" stroke="#fff" stroke-width="2"/></svg></a>
</section>

<div class="welcome-photo" role="img" aria-label="Business team meeting with a presenter at a flip chart"></div>
<section class="welcome">
  <h1>Welcome to Tessavale Communication</h1>
  <h2>Aenean erat arcu, euismod a ac cumsan sed pretium nec.</h2>
  <p>Mauris et nisl vel purus dapibus rhoncus ut eu urna. Vestibulum orci nisl, plac erat in ligula at, hendrerit dapibus diam.</p>
  <p>Nunc facilisis commodo maximus. Sed ligula urna, laoreet nec diam eu, varius vehicula tortor. Cras dictum tellus sit amet ipsum porta. Curabitur vel dignissim erat. Morbi lobortis lacinia dui, at porttitor libero semper vitae. In pulvinar enim metus. Vestibulum ante ipsum primis in faucibus orci luctus. Morbi lobortis felis et molestie condimentum vestibulum at, tristique tempus turpis.</p>
</section>

<aside class="news">
  <h3>Latest News</h3>
  <ul class="news-list">
    <li><span class="news-title">Praesent a velit diam</span><span class="news-date">Sep 6, 2014</span></li>
    <li><span class="news-title">Curabitur consequat quis</span><span class="news-date">Sep 6, 2014</span></li>
    <li><span class="news-title">Phasellus congue</span><span class="news-date">Sep 6, 2014</span></li>
  </ul>
</aside>

<footer class="site-footer">
  <div class="foot-col" style="left:97px;width:222px">
    <h4>About Us</h4>
    <p>Cras faucibus sapien at arcu dignissim interdum. Sed tempus leo nulla, eget auctor tortor pharetra a. Morbi et gravida tortor, vitae cursus odio amet felis eleifend molestie rutrum ante eu diam efficitur, non finibus diam rutrum</p>
    <a class="more" href="#">Know more</a>
  </div>
  <div class="divider" style="left:332px"></div>
  <div class="foot-col" style="left:357px;width:220px">
    <h4>Latest Blog</h4>
    <p class="lead">Morbi sit amet consequat diam</p>
    <p>Cras faucibus sapien at arcu dignissim interdum. Sed tempus leo nulla, eget auctor tortor pharetra a. Morbi et gravida tortor, vitae cursus odio amet felis eleifend molestie</p>
    <a class="more" href="#">Know more</a>
  </div>
  <div class="divider" style="left:596px"></div>
  <div class="foot-col" style="left:621px;width:200px">
    <h4>Email Signup</h4>
    <div class="signup-field">Name</div>
    <div class="signup-field">Email ID</div>
    <div class="signup-btn">SUBMIT</div>
  </div>
  <div class="divider" style="left:842px"></div>
  <div class="foot-col" style="left:870px;width:200px">
    <h4>Connect with us</h4>
    <ul class="social">
      <li><span class="badge" style="background:#3b5b98"></span>Join with us on<span class="net blue">Circlebook</span></li>
      <li><span class="badge" style="background:#35b3e6"></span>Follow us on<span class="net sky">Chatterline</span></li>
      <li><span class="badge" style="background:#1d78b4"></span>Share on<span class="net navy">Workweb</span></li>
      <li><span class="badge" style="background:#c7281f"></span>Watch on<span class="net red">ClipStream</span></li>
    </ul>
  </div>
</footer>

<div class="base-bar">
  <div class="base-nav">Home<span>|</span>About us<span>|</span>Services<span>|</span>Associates<span>|</span>Contact us</div>
  <div class="copyright">Copyright © 2014 Tessavale Communications. All rights reserved.</div>
</div>
</body>
</html>
```